Tradeshow Banner Design (Qty2, 6'H x 2'W)

Brightwell Contractors is an Electrical, Fire Alarm, and Security Contracting company. For tradeshows, we would like 2 vertical Banners to put behind our booth. Our colors are Red, Grey & Black. I would like the Banners to be informative on what services we provide, with some appealing Graphic Design. (bwc-kmo.com)
Slogan: Safeguarding Communities Electrical, Fire & Security Solutions
Target Market(s)
Commercial Construction Clients
Industry/Entity Type
Electrical / Construction
Font styles to use
Other font styles liked:
- Aileron
Colors
EB3D1F
EC4F4E
F09395
F8D3D4
FCEDEE
Requirements
Must have
- Our Logo, Color Scheme, Brief Caption of the services we provide
Nice to have
- Appealing Imagery & a modern/simplistic design

```html
<!DOCTYPE html>
<html lang="en">
<head>
<meta charset="utf-8">
<title>Brightwell Contractors – Tradeshow Banners</title>
<link rel="stylesheet" href="https://fonts.googleapis.com/css2?family=Montserrat:wght@300;400;500;600;700;800&family=Questrial&display=swap">
<style>
  :root {
    --red: #e8202a;
    --red-deep: #c81a22;
    --grey-dark: #3f3f42;
    --grey-text: #3a3a3c;
    --white: #ffffff;
    --canvas: #dcdddf;
  }
  html, body {
    margin: 0;
    padding: 0;
    overflow: hidden;
  }
  body {
    width: 1160px;
    height: 1200px;
    background: var(--canvas);
    position: relative;
    font-family: "Montserrat", sans-serif;
  }
  .banner {
    position: absolute;
    top: 30px;
    width: 380px;
    height: 1140px;
    overflow: hidden;
    box-shadow: 0 6px 24px rgba(0,0,0,0.12);
  }
  .banner--brand { left: 150px; }
  .banner--services { left: 630px; background: var(--white); }
  .banner-art {
    position: absolute;
    inset: 0;
    width: 380px;
    height: 1140px;
  }
  .layer { position: absolute; left: 0; width: 380px; text-align: center; }

  /* Brand banner */
  .brand-mark {
    top: 150px;
    left: 50%;
    width: 150px;
    height: 150px;
    margin-left: -75px;
    border-radius: 50%;
    background: var(--white);
  }
  .brand-name {
    top: 370px;
    color: var(--white);
    font-weight: 700;
    font-size: 39px;
    line-height: 42px;
    letter-spacing: 0.5px;
    text-transform: uppercase;
  }
  .brand-services {
    top: 460px;
    color: var(--white);
    font-size: 13px;
    font-weight: 400;
    letter-spacing: 0.3px;
  }
  .brand-headline {
    top: 765px;
    color: var(--white);
    font-size: 37px;
    line-height: 43px;
    font-weight: 500;
    letter-spacing: 0.5px;
  }
  .brand-headline strong { font-weight: 800; }
  .web-address {
    color: var(--white);
    font-weight: 300;
    font-size: 40px;
    letter-spacing: 0.5px;
  }
  .banner--brand .web-address { top: 962px; }

  /* Services banner */
  .services-headline {
    top: 318px;
    color: var(--grey-text);
    font-size: 41px;
    line-height: 43px;
    font-weight: 600;
    letter-spacing: 0.5px;
  }
  .services-headline .accent { color: var(--red); font-weight: 800; }
  .service-list {
    position: absolute;
    top: 545px;
    left: 42px;
    margin: 0;
    padding: 0;
    list-style: none;
  }
  .service-item {
    display: flex;
    align-items: center;
    height: 51px;
    font-family: "Questrial", sans-serif;
    font-size: 30px;
    color: var(--grey-text);
  }
  .service-icon { width: 46px; height: 46px; margin-right: 16px; flex: none; }
  .banner--services .web-address { top: 960px; }
</style>
</head>
<body>

<section class="banner banner--brand">
  <svg class="banner-art" viewBox="0 0 380 1140" aria-hidden="false">
    <defs>
      <linearGradient id="dusk-photo" x1="0" y1="0" x2="0" y2="1">
        <stop offset="0" stop-color="#3d5a86"/>
        <stop offset="0.45" stop-color="#4b4a44"/>
        <stop offset="1" stop-color="#1f3326"/>
      </linearGradient>
    </defs>
    <rect class="banner-field" width="380" height="1140" fill="var(--red)"/>
    <path class="photo-band" role="img" aria-label="Modern apartment buildings lit at dusk with landscaped gardens"
          d="M0 520 Q190 512 380 518 L380 722 Q180 705 0 728 Z" fill="url(#dusk-photo)"/>
    <path class="swoosh" d="M0 520 Q200 506 380 492 L380 518 Q190 512 0 520 Z" fill="var(--white)"/>
    <path class="swoosh" d="M0 748 Q170 710 380 712 L380 722 Q180 705 0 728 Z" fill="var(--white)"/>
    <rect class="rule" x="150" y="908" width="80" height="4" fill="var(--white)"/>
  </svg>

  <div class="brand-mark"></div>
  <div class="layer brand-name">Brightwell<br>Contractors</div>
  <div class="layer brand-services">ELECTRICAL | FIRE | SECURITY</div>
  <h2 class="layer brand-headline" style="margin:0">COMMERCIAL<br>PROPERTY<br><strong>PROTECTION</strong></h2>
  <div class="layer web-address">bwc-kmo.com</div>
</section>

<section class="banner banner--services">
  <svg class="banner-art" viewBox="0 0 380 1140">
    <defs>
      <linearGradient id="warehouse-photo" x1="0" y1="0" x2="1" y2="1">
        <stop offset="0" stop-color="#c9a064"/>
        <stop offset="0.5" stop-color="#8a6a4a"/>
        <stop offset="1" stop-color="#3a4f7a"/>
      </linearGradient>
      <linearGradient id="technician-photo" x1="0" y1="0" x2="1" y2="0">
        <stop offset="0" stop-color="#b0141b"/>
        <stop offset="0.6" stop-color="#d8242c"/>
        <stop offset="1" stop-color="#5a1518"/>
      </linearGradient>
    </defs>
    <path class="photo-top" role="img" aria-label="Warehouse aisle with racking and a ceiling security dome camera"
          d="M0 0 H380 V232 Q200 292 0 238 Z" fill="url(#warehouse-photo)"/>
    <path class="band-red" d="M0 238 Q200 292 380 232 L380 248 Q200 302 0 276 Z" fill="var(--red)"/>
    <rect class="rule" x="150" y="506" width="80" height="4" fill="var(--grey-dark)"/>
    <path class="band-grey" d="M0 870 Q190 808 380 826 L380 1140 L0 1140 Z" fill="var(--grey-dark)"/>
    <path class="photo-bottom" role="img" aria-label="Electrician working on a control panel, red duotone"
          d="M0 878 Q190 822 380 846 V1140 H0 Z" fill="url(#technician-photo)"/>
    <path d="M0 874 Q190 817 380 840" fill="none" stroke="var(--white)" stroke-width="4"/>
  </svg>

  <h2 class="layer services-headline" style="margin:0">WE HELP<br>OUR CLIENTS<br>GET <span class="accent">PEACE</span><br><span class="accent">OF MIND</span></h2>

  <ul class="service-list">
    <li class="service-item">
      <svg class="service-icon" viewBox="0 0 46 46"><circle cx="23" cy="23" r="21" fill="none" stroke="var(--grey-dark)" stroke-width="1.5"/><circle cx="23" cy="23" r="16" fill="var(--red)"/><path d="M25 12 L16 25 H22 L20 34 L30 20 H24 Z" fill="var(--white)"/></svg>
      Electrical
    </li>
    <li class="service-item">
      <svg class="service-icon" viewBox="0 0 46 46"><circle cx="23" cy="23" r="21" fill="none" stroke="var(--grey-dark)" stroke-width="1.5"/><path d="M23 10 L33 14 V22 Q33 31 23 36 Q13 31 13 22 V14 Z" fill="none" stroke="var(--red)" stroke-width="3"/><path d="M18 23 L22 27 L29 19" fill="none" stroke="var(--red)" stroke-width="3"/></svg>
      Security
    </li>
    <li class="service-item">
      <svg class="service-icon" viewBox="0 0 46 46"><circle cx="23" cy="23" r="21" fill="none" stroke="var(--grey-dark)" stroke-width="1.5"/><path d="M23 10 L33 14 V22 Q33 31 23 36 Q13 31 13 22 V14 Z" fill="none" stroke="var(--red)" stroke-width="3"/><path d="M23 17 V29 M17 23 H29" stroke="var(--red)" stroke-width="3"/></svg>
      Fire Protection
    </li>
    <li class="service-item">
      <svg class="service-icon" viewBox="0 0 46 46"><circle cx="23" cy="23" r="21" fill="none" stroke="var(--grey-dark)" stroke-width="1.5"/><circle cx="23" cy="23" r="11" fill="none" stroke="var(--red)" stroke-width="6" stroke-dasharray="4 3"/><circle cx="23" cy="23" r="8" fill="var(--red)"/><circle cx="23" cy="21" r="3" fill="var(--white)"/><path d="M18 28 Q23 22 28 28" fill="var(--white)"/></svg>
      Access Control
    </li>
    <li class="service-item">
      <svg class="service-icon" viewBox="0 0 46 46"><circle cx="23" cy="23" r="21" fill="none" stroke="var(--grey-dark)" stroke-width="1.5"/><rect x="12" y="13" width="18" height="16" fill="none" stroke="var(--red)" stroke-width="2.5"/><path d="M15 18 H27 M15 23 H23" stroke="var(--red)" stroke-width="2"/><path d="M31 22 V33" stroke="var(--red)" stroke-width="2"/><circle cx="28.5" cy="33" r="2.5" fill="var(--red)"/></svg>
      Audio Video
    </li>
  </ul>

  <div class="layer web-address">bwc-kmo.com</div>
</section>

</body>
</html>
```